Plumbing & Heating bussiness card design

i do all plumbing and heating work and need a catchy design. keep it simple but eye catching nothing gimicky
i do 24hr call outs
landlord safety checks
all aspects of plumbing and heating
boiler breakdowns
flue sure reg number 804617
i have put up my old card. not to bothered about the front but i have put up the back for the details. mobile number and office are the same and the email has changed to tolwenpipes@mailvoro.net

Industry/Entity Type

Safety

Contact Information for Business Card

i do 24hr call outs
landlord safety checks
boiler breakdowns

Requirements
Must have
• i do 24hr call outs
• landlord safety checks
• all aspects of plumbing and heating
• boiler breakdowns
• flue sure reg number 804617

```html
<!DOCTYPE html>
<html lang="en">
<head>
<meta charset="utf-8">
<title>A Tolwen Plumbing &amp; Heating – Business Card</title>
<link rel="stylesheet" href="https://fonts.googleapis.com/css2?family=Open+Sans:wght@400;600;700&display=swap">
<style>
  :root {
    --bg: #e9e6e1;
    --frame-red: #c8202f;
    --frame-blue: #2a86c8;
    --card: #ffffff;
    --ink: #1d1d1f;
    --logo-ink: #2e3035;
    --name-blue: #1b7cc3;
    --services-red: #c42032;
    --badge-fill: #dfe3e8;
  }
  html, body {
    margin: 0;
    width: 1200px;
    height: 960px;
    overflow: hidden;
    background: var(--bg);
    font-family: "Open Sans", Arial, sans-serif;
  }
  .card-frame {
    position: absolute;
    left: 110px;
    top: 150px;
    width: 980px;
    height: 660px;
    padding: 12px;
    box-sizing: border-box;
    background: linear-gradient(135deg, var(--frame-red) 0%, var(--frame-red) 35%, var(--frame-blue) 70%, var(--frame-blue) 100%);
  }
  .card {
    position: relative;
    width: 100%;
    height: 100%;
    background: var(--card);
    text-align: center;
    color: var(--ink);
  }
  .brand {
    position: absolute;
    top: 44px;
    left: 0;
    right: 0;
    font-weight: 700;
    color: var(--logo-ink);
    line-height: 1;
    text-transform: uppercase;
  }
  .brand-mark {
    display: block;
    width: 46px;
    height: 46px;
    margin: 0 auto 14px;
    border-radius: 50%;
    background: var(--logo-ink);
  }
  .brand-name { display: block; font-size: 78px; letter-spacing: -1px; }
  .brand-trade { display: block; font-size: 44px; margin-top: 6px; }
  .divider {
    position: absolute;
    top: 256px;
    left: 190px;
    width: 576px;
    height: 2px;
    background: var(--ink);
  }
  .contact {
    position: absolute;
    top: 276px;
    left: 0;
    right: 0;
  }
  .contact-name {
    margin: 0;
    font-size: 52px;
    font-weight: 600;
    color: var(--name-blue);
    line-height: 1.15;
  }
  .contact-role, .contact-line {
    margin: 4px 0 0;
    font-size: 27px;
    line-height: 1.3;
  }
  .services {
    position: absolute;
    bottom: 40px;
    left: 0;
    right: 0;
    margin: 0;
    font-size: 28px;
    line-height: 1.35;
    color: var(--services-red);
  }
  .reg {
    position: absolute;
    right: 44px;
    top: 330px;
    width: 128px;
    text-align: center;
  }
  .reg-number {
    display: block;
    font-size: 24px;
    font-weight: 600;
    margin-bottom: 8px;
  }
  .reg-badge {
    display: block;
    width: 112px;
    height: 112px;
    margin: 0 auto;
    background: var(--badge-fill);
  }
</style>
</head>
<body>
  <div class="card-frame">
    <section class="card">
      <div class="brand">
        <span class="brand-mark"></span>
        <span class="brand-name">A Tolwen</span>
        <span class="brand-trade">Plumbing &amp; Heating</span>
      </div>
      <div class="divider"></div>
      <div class="contact">
        <h1 class="contact-name">Owen R.Marlow</h1>
        <p class="contact-role">President &amp; CEO</p>
        <p class="contact-line">602-555-0174</p>
        <p class="contact-line">tolwenpipes@mailvoro.net</p>
        <p class="contact-line">www.tolwenplumbing.net</p>
      </div>
      <p class="services">i do 24hr call outs,landlord safety checks,all aspects of<br>plumbing and heating ,boiler breakdowns</p>
      <div class="reg">
        <span class="reg-number">804617</span>
        <span class="reg-badge" role="img" aria-label="Flue sure registration badge"></span>
      </div>
    </section>
  </div>
</body>
</html>
```